Corporate Web Redesign Project - coded

We would like redesign/refresh of our current site that would allow us to increase the depth of content and create a high quality impression for visitors.

Current site - http://corvanisystems.com/

A previous web redesign project has improved our site but it has not really reached the level we require.

Our customers are global, blue chip, organisations and a professional, corporate style of site is required.

Please note we would prefer a coded website to a just a design. We are happy to provide a zip of our current site if required.
Updates

                                   

Target Market(s)

Global oil and gas producers, KR, Tamberline, Orvadex etc.

Industry/Entity Type

It Professional

Requirements
Must have
• Design should support the level of content we currently have in the existing sitemap - although it should be expandable a site design for a large / complex site would not be appropriate

All current content / pages to be reflected in design

Must be visually appealing

Intuitive and clear navigation that is expandable

Display a high level of professionalism

Use a consistent palette of colours that complements our logo

Clean and organized layout

A way to capture visitor’s information or Call to action (i.e. contact link or form) on every page

Prominent Contact Information
Should not have
• Flash

```html
<!DOCTYPE html>
<html lang="en">
<head>
<meta charset="utf-8">
<title>Corvani Systems</title>
<link href="https://fonts.googleapis.com/css2?family=Open+Sans:ital,wght@0,400;0,600;0,700;1,400&display=swap" rel="stylesheet">
<style>
:root{
  --teal:#35b2c1;
  --teal-dark:#2a9aa8;
  --text:#555a5e;
  --heading:#2b2f33;
  --muted:#999;
  --line:#e0e0e0;
  --footer-bg:#f5f5f5;
  --bar-bg:#2c2c30;
  --white:#fff;
}
*{box-sizing:border-box;margin:0;padding:0}
html,body{width:1200px;height:1000px;overflow:hidden;background:var(--white);font-family:"Open Sans",sans-serif;color:var(--text)}
.page{position:relative;width:1200px;height:1000px}
.abs{position:absolute}

.intro{left:96px;top:4px;width:490px;font-size:13.5px;line-height:20px}
.checklist{left:613px;top:5px;list-style:none;font-size:13.5px}
.checklist li{display:flex;align-items:center;height:30px;gap:8px}

.cta{left:96px;top:106px;width:1010px;height:108px;border:1px solid var(--line);border-left:3px solid var(--teal);background:linear-gradient(#fff,#f9f9f9)}
.cta h2{position:absolute;left:28px;top:26px;font-size:23px;font-weight:400;color:var(--heading)}
.cta p{position:absolute;left:28px;top:65px;font-size:13px}
.btn{background:var(--teal);color:var(--white);font-weight:600;border:1px solid var(--teal-dark);border-radius:2px;display:flex;align-items:center;justify-content:center}
.cta .btn{position:absolute;left:847px;top:28px;width:132px;height:40px;font-size:14px}

.section-title{left:96px;top:254px;font-size:18px;color:var(--heading)}
.title-rule{left:212px;top:261px;width:894px;height:12px;background:#f0f0f0}

.client{width:150px;text-align:center;font-size:17px;font-weight:600;display:flex;align-items:center;justify-content:center;gap:6px;transform:translateX(-75px)}
.client .dot{width:12px;height:12px;border-radius:50%}

.footer{left:0;top:523px;width:1200px;height:413px;background:var(--footer-bg);border-top:1px solid var(--line)}
.col{position:absolute;top:36px}
.col h4{font-size:12.5px;font-weight:700;color:var(--heading);letter-spacing:.2px;margin-bottom:16px}
.links{list-style:none;font-size:13.5px;line-height:26px;color:var(--text)}
.contact{font-size:13px;line-height:20px;list-style:none}
.contact li{display:flex;gap:12px;margin-bottom:8px}
.contact li svg{flex:none;margin-top:4px}
.contact .gap{margin-top:22px}
.contact a{color:var(--teal);text-decoration:none}
.field{width:234px;height:33px;background:var(--white);border:1px solid #dcdcdc;margin-bottom:12px;display:flex;align-items:center;gap:8px;padding-left:10px;font-size:12.5px;font-style:italic;color:var(--muted)}
.field.message{height:110px;align-items:flex-start;padding-top:10px}
.col .btn{width:78px;height:34px;font-size:13.5px}

.bottom-bar{left:0;top:936px;width:1200px;height:64px;background:var(--bar-bg);font-size:12px;color:#7b7b80}
.bottom-bar .copy{position:absolute;left:96px;top:24px}
.bottom-bar .copy b{font-weight:400;color:#d6d6d6}
.follow{position:absolute;right:107px;top:22px;display:flex;align-items:center;gap:16px}
.follow span.icon{width:12px;height:12px;border-radius:50%;background:#6b6b70}
</style>
</head>
<body>
<div class="page">

  <p class="abs intro">Our solutions are used in more than 30 countries to support operations ranging from a single well to global deployments with Major Operators.</p>
  <ul class="abs checklist">
    <li><svg width="20" height="20" viewBox="0 0 20 20"><circle cx="10" cy="10" r="10" fill="var(--teal)"/><path d="M5.5 10.2l3 3 6-6" stroke="#fff" stroke-width="2.2" fill="none"/></svg>Training</li>
    <li><svg width="20" height="20" viewBox="0 0 20 20"><circle cx="10" cy="10" r="10" fill="var(--teal)"/><path d="M5.5 10.2l3 3 6-6" stroke="#fff" stroke-width="2.2" fill="none"/></svg>Business and Technical Consulting and Support</li>
  </ul>

  <div class="abs cta">
    <h2>The Business Of Drilling Wells</h2>
    <p>The success of the initiative is only as good as the process and the training of the people working the system.</p>
    <div class="btn">Know More!</div>
  </div>

  <h3 class="abs section-title">Our Clients</h3>
  <div class="abs title-rule"></div>

  <div class="abs client" style="left:185px;top:328px;color:#9fc6e6"><span class="dot" style="background:#f1b2b8"></span>Orvadex</div>
  <div class="abs client" style="left:390px;top:328px;color:#d9b98a">Velmora</div>
  <div class="abs client" style="left:597px;top:328px;color:#eedd8a">Ridgeway</div>
  <div class="abs client" style="left:802px;top:328px;color:#c9c9c9"><span class="dot" style="background:#f0c0c6"></span>Halden</div>
  <div class="abs client" style="left:1008px;top:328px;color:#c5e08c"><span class="dot" style="background:#f3eb8c"></span>KR</div>
  <div class="abs client" style="left:185px;top:426px;color:#a8c8e6">Nordquist</div>
  <div class="abs client" style="left:390px;top:426px;color:#a9bdb0">Brantor</div>

  <footer class="abs footer">
    <div class="col" style="left:96px">
      <h4>LINKS</h4>
      <ul class="links">
        <li>News</li><li>About Us</li><li>Time &amp; Cost Estimation</li><li>Materials &amp; Cost Control</li><li>Lessons Learned</li><li>Services &amp; Consulting</li>
      </ul>
    </div>
    <div class="col" style="left:354px">
      <h4>EUROPE CONTACT INFORMATION</h4>
      <ul class="contact">
        <li><svg width="14" height="14" viewBox="0 0 14 14"><path d="M7 1a4 4 0 0 0-4 4c0 3 4 8 4 8s4-5 4-8a4 4 0 0 0-4-4z" fill="#c4c4c4"/><circle cx="7" cy="5" r="1.5" fill="#f5f5f5"/></svg><span>18 Kestrel Row<br>Aberdeen AB12 4QT</span></li>
        <li class="gap"><svg width="14" height="12" viewBox="0 0 14 12"><rect x="0.5" y="1" width="13" height="10" fill="#c4c4c4"/><path d="M1 2l6 5 6-5" stroke="#f5f5f5" fill="none"/></svg><a>eu@corvanisystems.com</a></li>
        <li><svg width="14" height="14" viewBox="0 0 14 14"><path d="M3 1l3 3-2 2c1 2 2 3 4 4l2-2 3 3-2 2C6 13 1 8 1 3z" fill="#c4c4c4"/></svg><span>+44(0)1224&nbsp; 000481</span></li>
      </ul>
    </div>
    <div class="col" style="left:612px">
      <h4>NA CONTACT INFORMATION</h4>
      <ul class="contact">
        <li><svg width="14" height="14" viewBox="0 0 14 14"><path d="M7 1a4 4 0 0 0-4 4c0 3 4 8 4 8s4-5 4-8a4 4 0 0 0-4-4z" fill="#c4c4c4"/><circle cx="7" cy="5" r="1.5" fill="#f5f5f5"/></svg><span>4100 Meridian Park Dr Suite 210<br>Houston, TX 77059</span></li>
        <li class="gap"><svg width="14" height="12" viewBox="0 0 14 12"><rect x="0.5" y="1" width="13" height="10" fill="#c4c4c4"/><path d="M1 2l6 5 6-5" stroke="#f5f5f5" fill="none"/></svg><a>us@corvanisystems.com</a></li>
        <li><svg width="14" height="14" viewBox="0 0 14 14"><path d="M3 1l3 3-2 2c1 2 2 3 4 4l2-2 3 3-2 2C6 13 1 8 1 3z" fill="#c4c4c4"/></svg><span>(713) 555 0164</span></li>
      </ul>
    </div>
    <div class="col" style="left:870px">
      <h4>CONTACT FORM</h4>
      <div class="field"><svg width="12" height="12" viewBox="0 0 12 12"><circle cx="6" cy="3.5" r="3" fill="#c4c4c4"/><path d="M0 12c0-4 3-5 6-5s6 1 6 5z" fill="#c4c4c4"/></svg>Name (required)</div>
      <div class="field"><svg width="13" height="11" viewBox="0 0 14 12"><rect x="0.5" y="1" width="13" height="10" fill="#c4c4c4"/><path d="M1 2l6 5 6-5" stroke="#fff" fill="none"/></svg>E-mail (required)</div>
      <div class="field"><svg width="13" height="11" viewBox="0 0 14 12"><rect x="0.5" y="1" width="13" height="10" fill="#c4c4c4"/><path d="M1 2l6 5 6-5" stroke="#fff" fill="none"/></svg>Company (required)</div>
      <div class="field message"><svg width="12" height="12" viewBox="0 0 12 12"><path d="M1 11l1-3 6-6 2 2-6 6z" fill="#c4c4c4"/></svg>Message</div>
      <div class="btn">Send</div>
    </div>
  </footer>

  <div class="abs bottom-bar">
    <p class="copy">Copyright © 2013 <b>Corvani Systems</b>. All Right Reserved.</p>
    <div class="follow">Follow Us:
      <span class="icon" role="img" aria-label="Social profile"></span>
      <span class="icon" role="img" aria-label="Social profile"></span>
      <span class="icon" role="img" aria-label="Social profile"></span>
    </div>
  </div>

</div>
</body>
</html>
```